Brisk Harbor Packaging Design for RTE Beans

We need a product mock design that is aligned with our brand image. We need three SKUs. Black bean, Pinto bean, and Chickpeas. I've uploaded our brand logo here, Brisk Harbor. I have also took a screenshot of the design elements that we would like to see. The packaging die line can be seen on the file "packaging sample". Please refer to the screenshots for packaging design directions.

```html
<!DOCTYPE html>
<html lang="en">
<head>
<meta charset="utf-8">
<title>Brisk Harbor – Ranger Black Beans Pouch</title>
<link rel="stylesheet" href="https://fonts.googleapis.com/css2?family=Oswald:wght@600&family=Rokkitt:wght@600;700&family=Arimo:wght@400&display=swap">
<style>
  :root {
    --backdrop: #ebe8e4;
    --kraft: #c3ae8d;
    --kraft-light: #cdb99a;
    --kraft-edge: #9c8463;
    --ink: #3a2a26;
    --ink-soft: #4a3833;
    --photo-dark: #3b2a24;
    --photo-mid: #7b6f68;
    --photo-light: #b9b6b3;
  }
  * { box-sizing: border-box; margin: 0; padding: 0; }
  html, body { width: 1200px; height: 900px; overflow: hidden; background: var(--backdrop); }
  .stage { position: relative; width: 1200px; height: 900px; }

  .pouch {
    position: absolute; left: 440px; top: 207px; width: 307px; height: 534px;
    background: radial-gradient(ellipse at 50% 45%, var(--kraft-light) 0%, var(--kraft) 60%, var(--kraft-edge) 100%);
    box-shadow: inset 0 0 0 10px rgba(156,132,99,0.55), inset 0 0 26px rgba(90,70,50,0.35);
    color: var(--ink);
  }
  .pouch__zip {
    position: absolute; left: 10px; right: 10px; top: 28px; height: 1px;
    background: rgba(90,70,50,0.25);
  }
  .pouch__notch { position: absolute; top: 24px; width: 6px; height: 6px; background: var(--backdrop); border-radius: 50%; }
  .pouch__notch--left { left: -3px; }
  .pouch__notch--right { right: -3px; }

  .brand {
    position: absolute; left: 0; right: 0; top: 96px;
    display: flex; flex-direction: column; align-items: center; gap: 12px;
  }
  .brand__mark { width: 46px; height: 46px; border-radius: 50%; background: var(--ink-soft); }
  .brand__name {
    font-family: "Rokkitt", serif; font-weight: 700; font-size: 30px;
    letter-spacing: 1px; color: var(--ink); text-transform: uppercase; line-height: 1;
  }

  .star-row {
    position: absolute; left: 0; right: 0; top: 210px;
    text-align: center; font-size: 12px; letter-spacing: 7px; color: var(--ink);
    font-family: "Arimo", sans-serif;
  }

  .product-photo {
    position: absolute; left: 78px; top: 233px; width: 152px; height: 154px;
    border: 1px solid var(--ink);
    background: radial-gradient(ellipse at 45% 40%, var(--photo-dark) 0%, var(--photo-dark) 32%, var(--photo-mid) 60%, var(--photo-light) 100%);
  }
  .ornament {
    position: absolute; top: 268px; width: 24px; height: 24px;
    background: var(--ink-soft); border-radius: 3px; opacity: 0.8;
  }
  .ornament--left { left: 22px; }
  .ornament--right { right: 22px; }

  .product-name {
    position: absolute; left: 0; right: 0; top: 404px; text-align: center;
    font-family: "Oswald", sans-serif; font-weight: 600; font-size: 25px;
    line-height: 1; color: var(--ink); text-transform: uppercase; letter-spacing: 0.2px;
  }
  .product-desc {
    position: absolute; left: 0; right: 0; top: 432px; text-align: center;
    font-family: "Rokkitt", serif; font-weight: 600; font-size: 11px;
    line-height: 13px; letter-spacing: 1.7px; color: var(--ink); text-transform: uppercase;
  }
  .claims {
    position: absolute; left: 38px; right: 38px; top: 462px;
    display: flex; justify-content: space-between; align-items: center;
    font-family: "Arimo", sans-serif; font-size: 8.5px; color: var(--ink); text-transform: uppercase;
  }
  .claims__stars { font-size: 5px; letter-spacing: 2px; }
</style>
</head>
<body>
<div class="stage">
  <div class="pouch">
    <span class="pouch__notch pouch__notch--left"></span>
    <span class="pouch__notch pouch__notch--right"></span>
    <div class="pouch__zip"></div>

    <div class="brand">
      <span class="brand__mark"></span>
      <span class="brand__name">Brisk Harbor</span>
    </div>

    <div class="star-row">★★★★★★★★★</div>

    <div class="ornament ornament--left" role="img" aria-label="Western star ornament"></div>
    <div class="product-photo" role="img" aria-label="Photo of cooked black beans heaped on a metal spoon"></div>
    <div class="ornament ornament--right" role="img" aria-label="Western star ornament"></div>

    <h1 class="product-name">Ranger Black Beans</h1>
    <p class="product-desc">Slow simmered with onions<br>bell pappers and spices</p>
    <div class="claims">
      <span>Non-GMO</span>
      <span class="claims__stars">★★★★★★★★★</span>
      <span>Plant Protein</span>
    </div>
  </div>
</div>
</body>
</html>
```